simple non-fiction book illustrations - line drawings

Take my 9 simple drawings and make them look good! Need 300dpi line drawing illustrations, eps or png with transparency, in consistent, simple style, for inclusion in non-fiction book. Images supplied are from a range of sources, need to be redrawn to look professional and consistent. The book is called Ink With Purpose: Shrewd methods of outlining, drafting pages which earn more in one's trade.

Target Market(s)

business people wishing to write a book

Font styles to use
Serif

Colors
1b1b1b
919191
d3d3d3
ffffff

Requirements
Must have
• print-resolution (300dpi) image file and application files (ideally Adobe Illustrator).

```html
<!DOCTYPE html>
<html lang="en">
<head>
<meta charset="utf-8">
<title>Ink With Purpose – Figures</title>
<link href="https://fonts.googleapis.com/css2?family=Open+Sans:wght@400;600;700&display=swap" rel="stylesheet">
<style>
  :root {
    --ink: #1b1b1b;
    --mid: #919191;
    --light: #d3d3d3;
    --paper: #ffffff;
  }
  html, body {
    margin: 0;
    padding: 0;
    width: 1013px;
    height: 1200px;
    overflow: hidden;
    background: var(--paper);
  }
  .figure-sheet {
    display: block;
    width: 1013px;
    height: 1200px;
    font-family: "Open Sans", Arial, sans-serif;
  }
  .line { fill: none; stroke: var(--ink); stroke-width: 3; stroke-linecap: round; }
  .axis-guide { stroke: var(--light); stroke-width: 1.5; }
  .label-soft { fill: var(--mid); font-size: 17px; letter-spacing: 0.5px; }
  .label-strong { fill: var(--ink); font-size: 19px; letter-spacing: 0.5px; }
  .ring-base { fill: var(--light); }
  .ring-dash { fill: none; stroke: var(--paper); stroke-width: 1.5; stroke-dasharray: 5 4; }
  .ring-core { fill: var(--paper); stroke: var(--mid); stroke-width: 3; }
  .node { fill: var(--mid); }
  .node-text { fill: var(--paper); font-size: 9.5px; text-anchor: middle; }
  .core-text { fill: var(--ink); font-size: 14px; text-anchor: middle; }
  .ring-caption { fill: var(--paper); font-size: 8.5px; letter-spacing: 0.4px; }
  .spoke { stroke: var(--mid); stroke-width: 1.5; marker-end: url(#spoke-head); }
  .venn-set { fill: var(--light); mix-blend-mode: multiply; }
  .venn-text { fill: var(--ink); font-size: 13.5px; }
  .chart-axis { stroke: var(--mid); stroke-width: 2; fill: none; }
  .chart-split { stroke: var(--mid); stroke-width: 1.5; stroke-dasharray: 4 4; }
  .chart-mark { fill: var(--ink); font-size: 19px; text-anchor: middle; }
  .chart-quadrant { fill: var(--ink); font-size: 23px; font-weight: 700; text-anchor: middle; }
  .chart-label { fill: var(--ink); font-size: 12px; }
  .map-panel { fill: var(--light); }
  .map-divider { stroke: var(--paper); stroke-width: 2; }
  .map-text { fill: var(--paper); font-size: 14px; text-anchor: middle; letter-spacing: 0.3px; }
</style>
</head>
<body>
<svg class="figure-sheet" viewBox="0 0 1160 1374" xmlns="http://www.w3.org/2000/svg">
  <defs>
    <marker id="spoke-head" viewBox="0 0 10 10" refX="5" refY="5" markerWidth="5" markerHeight="5" orient="auto">
      <path d="M0 0 L10 5 L0 10 Z" fill="#919191"/>
    </marker>
    <marker id="axis-head" viewBox="0 0 10 10" refX="5" refY="5" markerWidth="6" markerHeight="6" orient="auto">
      <path d="M0 0 L10 5 L0 10 Z" fill="#919191"/>
    </marker>
    <path id="caption-arc" d="M 128.6 752.7 A 152 152 0 0 0 361.4 752.7"/>
  </defs>

  <!-- Figure: shell -->
  <g class="figure-shell">
    <rect x="65" y="65" width="442" height="345" rx="8" fill="#d3d3d3" role="img" aria-label="Line drawing of a spiral seashell seen in cross-section, showing its chambers"/>
  </g>

  <!-- Figure: growth spiral -->
  <g class="figure-spiral">
    <line class="axis-guide" x1="568" y1="188" x2="1133" y2="188"/>
    <line class="axis-guide" x1="813" y1="8" x2="813" y2="458"/>
    <path class="line" d="M1072 188
      A218 218 0 0 1 636 188
      A147 147 0 0 1 930 188
      A90 90 0 0 1 750 188
      A56 56 0 0 1 862 188
      A36 36 0 0 1 790 188
      A20 20 0 0 1 830 188
      A12 12 0 0 1 806 188
      A6 6 0 0 1 818 188"/>
    <text class="label-soft" text-anchor="middle" transform="translate(673 74) rotate(-43)">YOURSELF</text>
    <text class="label-soft" text-anchor="middle" transform="translate(918 98) rotate(56)">YOUR BUSINESS</text>
    <text class="label-strong" text-anchor="middle" transform="translate(940 264) rotate(-54)">WRITING YOUR BOOK</text>
    <text class="label-soft" text-anchor="middle" transform="translate(1008 360) rotate(138)">YOUR PLATFORM</text>
    <text class="label-soft" text-anchor="middle" transform="translate(662 342) rotate(-130)">YOUR NETWORK</text>
  </g>

  <!-- Figure: relationship rings -->
  <g class="figure-rings">
    <circle class="ring-base" cx="245" cy="655" r="180"/>
    <circle class="ring-dash" cx="245" cy="655" r="163"/>
    <circle class="ring-core" cx="245" cy="655" r="82"/>
    <text class="ring-caption"><textPath href="#caption-arc" startOffset="50%" text-anchor="middle">PEOPLE YOU DON'T NOW YET</textPath></text>

    <g class="spokes">
      <line class="spoke" x1="230" y1="518" x2="222" y2="498"/>
      <line class="spoke" x1="245" y1="515" x2="245" y2="495"/>
      <line class="spoke" x1="260" y1="518" x2="268" y2="498"/>
      <line class="spoke" x1="355" y1="598" x2="370" y2="580"/>
      <line class="spoke" x1="362" y1="610" x2="382" y2="600"/>
      <line class="spoke" x1="364" y1="624" x2="386" y2="626"/>
      <line class="spoke" x1="320" y1="742" x2="340" y2="736"/>
      <line class="spoke" x1="312" y1="748" x2="320" y2="766"/>
      <line class="spoke" x1="298" y1="750" x2="300" y2="770"/>
      <line class="spoke" x1="166" y1="742" x2="152" y2="755"/>
      <line class="spoke" x1="178" y1="749" x2="172" y2="768"/>
      <line class="spoke" x1="194" y1="750" x2="200" y2="770"/>
      <line class="spoke" x1="130" y1="597" x2="118" y2="580"/>
      <line class="spoke" x1="124" y1="610" x2="104" y2="604"/>
      <line class="spoke" x1="123" y1="625" x2="102" y2="628"/>
    </g>

    <circle class="node" cx="245" cy="550" r="33"/>
    <text class="node-text" x="245" y="547">PARTNERS</text>
    <text class="node-text" x="245" y="559">&amp; SUPPLIERS</text>

    <circle class="node" cx="330" cy="617" r="33"/>
    <text class="node-text" x="330" y="614">SOCIAL MEDIA</text>
    <text class="node-text" x="330" y="626">FOLLOWERS</text>

    <circle class="node" cx="298" cy="717" r="33"/>
    <text class="node-text" x="298" y="714">INDUSTRY</text>
    <text class="node-text" x="298" y="726">PEERS</text>

    <circle class="node" cx="188" cy="717" r="33"/>
    <text class="node-text" x="188" y="714">CONNECTORS</text>
    <text class="node-text" x="188" y="726">&amp; MENTORS</text>

    <circle class="node" cx="155" cy="617" r="33"/>
    <text class="node-text" x="155" y="614">USEFUL</text>
    <text class="node-text" x="155" y="626">CONTACTS</text>

    <text class="core-text" x="245" y="644">CORE</text>
    <text class="core-text" x="245" y="661">RELATIONSHIPS</text>
  </g>

  <!-- Figure: overlap of expertise, needs and future -->
  <g class="figure-venn" style="isolation:isolate">
    <circle class="venn-set" cx="813" cy="577" r="108"/>
    <circle class="venn-set" cx="724" cy="705" r="92"/>
    <circle class="venn-set" cx="888" cy="707" r="108"/>
    <text class="venn-text" x="767" y="562">MY EXPERTISE</text>
    <text class="venn-text" x="670" y="711">MY</text>
    <text class="venn-text" x="670" y="727">CUSTOMERS</text>
    <text class="venn-text" x="670" y="743">NEEDS</text>
    <text class="venn-text" x="862" y="711">THE FUTURE:</text>
    <text class="venn-text" x="862" y="730">- INDUSTRY</text>
    <text class="venn-text" x="862" y="746">- BUSINESS</text>
    <text class="venn-text" x="862" y="762">- CUSTOMERS</text>
  </g>

  <!-- Figure: effort / revenue matrix -->
  <g class="figure-matrix">
    <line class="chart-axis" x1="65" y1="1290" x2="65" y2="945" marker-end="url(#axis-head)"/>
    <line class="chart-axis" x1="65" y1="1290" x2="410" y2="1290" marker-end="url(#axis-head)"/>
    <line class="chart-split" x1="233" y1="950" x2="233" y2="1290"/>
    <line class="chart-split" x1="65" y1="1113" x2="405" y2="1113"/>
    <text class="chart-label" transform="translate(53 1075) rotate(-90)">REVENUE IMPACT</text>
    <text class="chart-label" x="337" y="1311">EFFORT</text>

    <text class="chart-quadrant" x="197" y="1089">1</text>
    <text class="chart-quadrant" x="268" y="1089">2</text>
    <text class="chart-quadrant" x="197" y="1154">3</text>
    <text class="chart-quadrant" x="268" y="1154">4</text>

    <text class="chart-mark" x="147" y="1024">x</text>
    <text class="chart-mark" x="114" y="1089">x</text>
    <text class="chart-mark" x="311" y="1046">x</text>
    <text class="chart-mark" x="345" y="1089">x</text>
    <text class="chart-mark" x="129" y="1154">x</text>
    <text class="chart-mark" x="311" y="1176">x</text>
    <text class="chart-mark" x="196" y="1219">x</text>
    <text class="chart-mark" x="279" y="1219">x</text>
  </g>

  <!-- Figure: customer empathy map -->
  <g class="figure-empathy">
    <rect class="map-panel" x="635" y="953" width="355" height="277"/>
    <rect class="map-panel" x="635" y="1232" width="177" height="56"/>
    <rect class="map-panel" x="814" y="1232" width="176" height="56"/>
    <line class="map-divider" x1="635" y1="953" x2="990" y2="1230"/>
    <line class="map-divider" x1="990" y1="953" x2="635" y2="1230"/>
    <circle cx="812" cy="1091" r="58" fill="#ffffff"/>
    <text class="map-text" x="812" y="999">THINK &amp; FEEL?</text>
    <text class="map-text" x="702" y="1098">HEAR?</text>
    <text class="map-text" x="930" y="1098">SEE?</text>
    <text class="map-text" x="812" y="1196">SAY &amp; DO?</text>
    <text class="map-text" x="723" y="1266">PAIN</text>
    <text class="map-text" x="902" y="1266">GAIN</text>
  </g>
</svg>
</body>
</html>
```